Business Profile Landing Page for search engine Start UP " Ember Gate"

Hi there
Ember Gate is an search engine for the Ember Gate - business.

What i´m looking for is a stunning singel Profile Landing Page for the Companys presentation.

Following Details should be included.

1st section
Comapanys name
Adress
info row ( opening time or what ever)
Profile Picture Big ( Could be the logo)
+3 smaller Pictures ( Maybe the store, main product ...)

2nd Section
navigation Icons for:
Call, Mail , Web, Route, Data

3er Section
About us.

Text lines.....
+Pictures slider

4th Section
1 row : Products ( Titel , Picture, Price)
2nd row :Service ( same as Products + text lines )

5th section
Blog Posts row

.....................................................
Well thats all, Colors used from the logo, u can also use the favicon somewhere (the crown magnifying glass)

Target Market(s)

All Comapnys, it should be an " used for all" design

Number of Pages Required

1 page

Requirements
Must have
• The first sighting is the important part, so the " first section should be impressively and makes the customers curious about more informations (very important for mobile version)
Nice to have
• If you can insert our favicon somewhere would be cool, but its not nessesery
Should not have
• you dont need to make a header or footer, that part is already done. i just need the main section design

```html
<!DOCTYPE html>
<html lang="en">
<head>
<meta charset="utf-8">
<title>Ember Gate – Business Profile</title>
<link href="https://fonts.googleapis.com/css2?family=Inter:wght@400;500;600&display=swap" rel="stylesheet">
<style>
  :root {
    --navy: #13203a;
    --navy-soft: #1d2b4a;
    --yellow: #e2dd48;
    --gold: #d4b42a;
    --white: #ffffff;
    --paper: #f9f9fa;
    --ink: #222222;
    --text-light: #e6e8ee;
    --muted: #a3a8b3;
  }
  * { box-sizing: border-box; margin: 0; padding: 0; }
  html, body { width: 1200px; height: 1200px; overflow: hidden; }
  body { font-family: "Inter", sans-serif; background: var(--paper); position: relative; }

  .top-bar { position: absolute; left: 0; top: 0; width: 1200px; height: 67px; background: var(--white); }
  .brand { position: absolute; left: 81px; top: 20px; font-size: 22px; font-weight: 600; color: var(--ink); letter-spacing: -0.2px; }

  .hero { position: absolute; left: 0; top: 67px; width: 1200px; height: 804px; background: var(--navy); overflow: hidden; }
  .hero-title { position: absolute; left: 68px; top: 110px; font-size: 58px; line-height: 62px; font-weight: 500; color: var(--white); letter-spacing: 0.3px; }
  .hero-title .accent { color: var(--yellow); }
  .hero-lead { position: absolute; left: 68px; top: 334px; font-size: 20px; font-weight: 500; color: var(--text-light); letter-spacing: 0.4px; }

  .search-field { position: absolute; left: 68px; top: 403px; width: 370px; height: 53px; background: var(--white); border-radius: 5px; padding-left: 20px; display: flex; align-items: center; font-size: 16px; color: var(--muted); letter-spacing: 0.5px; }
  .search-button { position: absolute; left: 470px; top: 403px; width: 134px; height: 53px; border: 2px solid var(--gold); border-radius: 5px; display: flex; align-items: center; justify-content: center; gap: 10px; font-size: 18px; font-weight: 500; color: var(--yellow); letter-spacing: 0.6px; }
  .search-button .dot { width: 10px; height: 10px; border-radius: 50%; background: var(--gold); }

  .hero-backdrop { position: absolute; left: 651px; top: 253px; width: 446px; height: 413px; background: var(--navy-soft); border-radius: 223px 223px 0 0; }
  .hero-photo { position: absolute; left: 661px; top: 166px; width: 426px; height: 500px; border-radius: 200px 200px 0 0; background: linear-gradient(180deg, #2a2624 0%, #5a3b2c 45%, #2f5a4c 75%, #24463c 100%); }

  .info-row { position: absolute; left: 0; top: 700px; width: 1200px; }
  .info-col { position: absolute; top: 0; }
  .info-col h3 { font-size: 20px; font-weight: 500; color: var(--white); letter-spacing: 0.6px; }
  .info-col p { margin-top: 14px; font-size: 17px; line-height: 25px; color: var(--text-light); letter-spacing: 0.4px; }
  .col-address { left: 68px; }
  .col-hours { left: 395px; }
  .col-contact { left: 715px; }
  .map-link { position: absolute; left: 992px; top: 0; display: flex; align-items: center; gap: 6px; font-size: 20px; font-weight: 500; color: var(--white); letter-spacing: 0.5px; }
  .map-thumb { position: absolute; left: 1049px; top: 27px; width: 59px; height: 58px; background: linear-gradient(135deg, #e9ecef, #d6dde6 60%, #f1e2b8); border: 1px solid #c9ced6; }

  .about { position: absolute; left: 0; top: 871px; width: 1200px; height: 329px; background: var(--paper); }
  .about-visual { position: absolute; left: 97px; top: 123px; width: 363px; height: 206px; background: linear-gradient(180deg, #e7e8ea 0%, #cfcfd1 55%, #9d9ea2 100%); border-radius: 6px 6px 0 0; }
  .about-title { position: absolute; left: 621px; top: 86px; font-size: 40px; line-height: 50px; font-weight: 500; color: var(--ink); letter-spacing: 0.5px; }
  .about-title .accent { color: var(--yellow); }
  .about-text { position: absolute; left: 621px; top: 214px; width: 430px; font-size: 19.5px; line-height: 29px; color: #3a3a3a; letter-spacing: 0.3px; }
</style>
</head>
<body>
  <header class="top-bar">
    <div class="brand">Ember Gate</div>
  </header>

  <section class="hero">
    <h1 class="hero-title">Find your best local<br>business with<br><span class="accent">Ember Gate</span></h1>
    <p class="hero-lead">Search now and bring something best to your home</p>
    <div class="search-field">Type here</div>
    <div class="search-button"><span class="dot"></span>search</div>

    <div class="hero-backdrop"></div>
    <div class="hero-photo" role="img" aria-label="Photo of a smiling woman with curly hair and glasses looking at her smartphone"></div>

    <div class="info-row">
      <div class="info-col col-address">
        <h3>Ember Gate</h3>
        <p>48 Harbour Lane,<br>Wexley, NSW 2290</p>
      </div>
      <div class="info-col col-hours">
        <h3>Opening hours</h3>
        <p>Monday - Saturday<br>8:00 am - 6:00 pm</p>
      </div>
      <div class="info-col col-contact">
        <h3>Contact</h3>
        <p>02 5550 1427<br>www.embergate.com</p>
      </div>
      <div class="map-link">
        <svg width="22" height="16" viewBox="0 0 22 16" aria-hidden="true">
          <path d="M1.5 8 C5 2.5 17 2.5 20.5 8 C17 13.5 5 13.5 1.5 8 Z" fill="none" stroke="#ffffff" stroke-width="1.8"/>
          <circle cx="11" cy="8" r="3" fill="none" stroke="#ffffff" stroke-width="1.8"/>
        </svg>
        view map
      </div>
      <div class="map-thumb" role="img" aria-label="Small street map preview of the business location"></div>
    </div>
  </section>

  <section class="about">
    <div class="about-visual" role="img" aria-label="Excited man in a grey t-shirt beside a card showing the search page"></div>
    <h2 class="about-title">What is<br><span class="accent">Ember Gate</span> ?</h2>
    <p class="about-text">Lorem ipsum dolor sit amet, consectetur adipiscing elit. Ut eu aliquam risus, donec maecenas neque amet, non. Molestie pretium facilisi praesent interdum</p>
  </section>
</body>
</html>
```